Keystone Draftworks - business cards
A set of business cards for a company
Dear designers,
I suggest that we minimize the quantity of red and grey filled areas on the cards.
I favour more the versions where there is more white space and just some colored accents.
In my opinion it looks more appropriate for our corporate customers.
Thanks for your understanding.
It might be a good idea to print a QR code on the back side of the card if it fits logically.
Not necessary but I'd like to see some ideas with and without it.

```html
<!DOCTYPE html>
<html lang="en">
<head>
<meta charset="utf-8">
<title>Keystone Draftworks – business cards</title>
<link href="https://fonts.googleapis.com/css2?family=Arimo:wght@400;700&display=swap" rel="stylesheet">
<style>
  :root {
    --bg: #ecebe8;
    --card: #ffffff;
    --red: #c3142d;
    --red-dark: #6e0712;
    --grey: #9a9ca0;
    --ink: #2b2b2b;
    --on-red: #ffffff;
  }
  * { margin: 0; padding: 0; box-sizing: border-box; }
  html, body { width: 1200px; height: 852px; overflow: hidden; background: var(--bg); }
  body { position: relative; font-family: "Arimo", Arial, sans-serif; }

  .card {
    position: absolute;
    width: 576px; height: 336px;
    background: var(--card);
    border-radius: 16px;
    overflow: hidden;
    box-shadow: 0 6px 18px rgba(0,0,0,.18);
  }
  .card--front { left: 130px; top: 130px; }
  .card--reverse { left: 494px; top: 440px; }

  .card__shape { position: absolute; inset: 0; width: 100%; height: 100%; }

  .contact { position: absolute; color: var(--on-red); font-size: 13px; line-height: 1.45; }
  .contact__name { font-weight: 700; font-size: 17px; }
  .contact__role { font-weight: 700; font-size: 12px; margin-bottom: 46px; }
  .contact__address { margin-bottom: 14px; }
  .contact__line { display: flex; align-items: center; gap: 8px; font-size: 12.5px; }
  .contact__line svg { width: 12px; height: 12px; flex: none; }

  .card--front .contact { left: 24px; top: 28px; }
  .card--reverse .contact { right: 28px; top: 28px; text-align: right; }
  .card--reverse .contact__name,
  .card--reverse .contact__role { color: var(--ink); }
  .card--reverse .contact__line { justify-content: flex-end; }

  .brand {
    position: absolute;
    display: flex; align-items: center; gap: 10px;
    color: var(--red);
    font-weight: 700;
    font-size: 25px;
    letter-spacing: .5px;
    text-transform: uppercase;
    line-height: 1.05;
  }
  .brand__dot { width: 18px; height: 18px; border-radius: 50%; background: var(--red); flex: none; }
  .card--front .brand { left: 344px; top: 140px; }
  .card--reverse .brand { left: 40px; top: 196px; }
</style>
</head>
<body>

<!-- Front card: red contact panel on the left -->
<section class="card card--front">
  <svg class="card__shape" viewBox="0 0 576 336" aria-hidden="true">
    <defs>
      <radialGradient id="redGlowA" cx="35%" cy="50%" r="70%">
        <stop offset="0" stop-color="#d41a34"/>
        <stop offset="1" stop-color="#6e0712"/>
      </radialGradient>
    </defs>
    <path d="M0 0 H262 C330 90 240 250 312 336 H0 Z" fill="url(#redGlowA)"/>
    <path d="M270 0 C340 90 250 250 322 336" fill="none" stroke="#b9bbbf" stroke-width="7"/>
  </svg>
  <div class="contact">
    <div class="contact__name">Tobias Varen</div>
    <div class="contact__role">Director</div>
    <div class="contact__address">Cobalt Lane, 1<br>Easton, 482150 Norland</div>
    <div class="contact__line"><svg viewBox="0 0 12 12"><rect x="3" y="1" width="6" height="10" rx="1.5" fill="#fff"/></svg>+7 900 555-0136</div>
    <div class="contact__line"><svg viewBox="0 0 12 12"><rect x="3" y="1" width="6" height="10" rx="1.5" fill="#fff"/></svg>+7 900 555-0172</div>
    <div class="contact__line"><svg viewBox="0 0 12 12"><rect x="1" y="3" width="10" height="7" rx="1" fill="#fff"/></svg>+7 900 555-0136</div>
    <div class="contact__line"><svg viewBox="0 0 12 12"><rect x="1" y="2.5" width="10" height="7" fill="#fff"/><path d="M1 2.5 L6 7 L11 2.5" fill="none" stroke="#8c0c1c" stroke-width="1"/></svg>t.varen@keystonedw.com</div>
    <div class="contact__line"><svg viewBox="0 0 12 12"><circle cx="6" cy="6" r="5" fill="#fff"/></svg>www.keystonedw.com</div>
  </div>
  <div class="brand"><span class="brand__dot"></span><span>Keystone<br>Draftworks</span></div>
</section>

<!-- Reverse layout: logo left, red contact panel right -->
<section class="card card--reverse">
  <svg class="card__shape" viewBox="0 0 576 336" aria-hidden="true">
    <defs>
      <radialGradient id="redGlowB" cx="70%" cy="55%" r="70%">
        <stop offset="0" stop-color="#d41a34"/>
        <stop offset="1" stop-color="#6e0712"/>
      </radialGradient>
    </defs>
    <path d="M576 0 H300 C220 30 330 260 262 336 H576 Z" fill="url(#redGlowB)" transform="translate(0,0)"/>
    <path d="M292 0 C212 30 322 260 254 336" fill="none" stroke="#b9bbbf" stroke-width="7"/>
  </svg>
  <div class="contact">
    <div class="contact__name" style="color:var(--on-red)">Tobias Varen</div>
    <div class="contact__role" style="color:var(--on-red)">Director</div>
    <div class="contact__address">Cobalt Lane, 1<br>Easton, 482150 Norland</div>
    <div class="contact__line">+7 900 555-0136<svg viewBox="0 0 12 12"><rect x="3" y="1" width="6" height="10" rx="1.5" fill="#fff"/></svg></div>
    <div class="contact__line">+7 900 555-0172<svg viewBox="0 0 12 12"><rect x="3" y="1" width="6" height="10" rx="1.5" fill="#fff"/></svg></div>
    <div class="contact__line">+7 900 555-0136<svg viewBox="0 0 12 12"><rect x="1" y="3" width="10" height="7" rx="1" fill="#fff"/></svg></div>
    <div class="contact__line">t.varen@keystonedw.com<svg viewBox="0 0 12 12"><rect x="1" y="2.5" width="10" height="7" fill="#fff"/><path d="M1 2.5 L6 7 L11 2.5" fill="none" stroke="#8c0c1c" stroke-width="1"/></svg></div>
    <div class="contact__line">www.keystonedw.com<svg viewBox="0 0 12 12"><circle cx="6" cy="6" r="5" fill="#fff"/></svg></div>
  </div>
  <div class="brand"><span class="brand__dot"></span><span>Keystone<br>Draftworks</span></div>
</section>

</body>
</html>
```